Inspiring Wordpress Design for Brightpath Figure Renewal: Assured Contest

We need a web design for a medical weight loss clinic near San Francisco. We would like for our site to be similar to http://www.trimlarkhaven.com:

The winning design will communicate a youthful, energetic, and fun vibe. We want to imply success and vitality in contrast to the guilt, shame, and burden of traditional weight loss. At the same time, it is a very scientifically oriented and physician supervised so we need it to convey authority and science at the same time.

Our logo and font files are attached.

Target Demographic: 30-50 year old women of White, Asian, Latin, and African American Backgrounds. Income $35-120k.

Target Market(s)

We are a medical Weight Loss Center. Our target audience is women aged 30-55 in low middle to middle class, incomes from $30k to $150k per year. Target Audience is of mixed race including white, Latin, African American and Asian.

Industry/Entity Type

Clinic

Font styles to use
Other font styles liked:
• 738162 Acrom Family (OTF) $160.00 The Velvet Quarry Ltd package Desktop users: 10 - 915374 Twentieth Century 1 Volume (OTF) $157.00 Glyphorra package Desktop users: 5 - 608293 Twentieth Century 2 Volume (Win TTF) $105.00 Glyphorra package

Requirements
Must have
• Tabs:
Science of Weight Loss Success
Success Stories
Location and Hours
Contact Us
Espanol

Need an Area for Our Slogan ( exact slogan TBD)

Please include Stock Images and links to those images in your design.

We would Like to Include Three Buttons in the design:
1. Stop the Low Calorie Starvation Diet
2. Why Coral Bayslim
3. Become a Skinny Fat Burner Today
Nice to have
• Fonts that we have purchased are attached. Please use these.

```html
<!DOCTYPE html>
<html lang="en">
<head>
<meta charset="utf-8">
<title>Coral Bayslim</title>
<link rel="stylesheet" href="https://fonts.googleapis.com/css2?family=Quicksand:wght@400;500;600;700&display=swap">
<style>
  :root {
    --teal: #2dbcb4;
    --orange: #f5a623;
    --orange-light: #f6c866;
    --blue-top: #8fb0e0;
    --blue-bottom: #3761b8;
    --green-top: #b4e07a;
    --green-bottom: #7cc02a;
    --welcome-green: #8cc63f;
    --panel-grey: #dfe3e3;
    --hero-grey: #d5d9d9;
    --text: #222;
    --white: #fff;
  }
  * { box-sizing: border-box; margin: 0; padding: 0; }
  html, body { width: 1000px; height: 1200px; overflow: hidden; }
  body { position: relative; background: var(--white); font-family: "Quicksand", sans-serif; color: var(--text); }

  .site-header { position: absolute; left: 0; top: 0; width: 1000px; height: 150px; }
  .brand { position: absolute; left: 64px; top: 44px; display: flex; align-items: center; gap: 12px;
    font-size: 44px; font-weight: 500; color: var(--orange); letter-spacing: -0.5px; }
  .brand-dot { width: 16px; height: 16px; border-radius: 50%; background: var(--teal); }

  .main-nav { position: absolute; left: 0; top: 150px; width: 1000px; height: 99px; background: var(--teal); }
  .nav-tab { position: absolute; top: 0; height: 99px; display: flex; align-items: center; justify-content: center;
    text-align: center; color: var(--white); font-size: 16px; line-height: 21px; letter-spacing: 0.3px;
    border-left: 1px solid rgba(255,255,255,0.35); }
  .nav-tab.is-active { border-top: 3px solid var(--orange); }
  .nav-end { position: absolute; left: 950px; top: 0; height: 99px; border-left: 1px solid rgba(255,255,255,0.35); }

  .hero { position: absolute; left: 0; top: 249px; width: 1000px; height: 401px;
    background: linear-gradient(to bottom, var(--hero-grey) 0%, #fafafa 40%, #fff 58%, var(--hero-grey) 100%); }
  .slogan { position: absolute; left: 60px; top: 88px; color: var(--teal); font-size: 54px; font-weight: 500; line-height: 56px; }
  .slogan span { display: block; padding-left: 180px; }
  .hero-photo { position: absolute; left: 679px; top: 1px; width: 256px; height: 308px;
    background: linear-gradient(to bottom, #f4f4f4, #e9e2ea 60%, #d6b5dc); }

  .cta { position: absolute; top: 558px; width: 283px; height: 133px; border-radius: 20px; padding: 14px 18px;
    color: var(--white); font-size: 29px; line-height: 33px; letter-spacing: 0.5px;
    text-shadow: 1px 1px 2px rgba(0,0,0,0.35); border: 2px solid; }
  .cta strong { font-weight: 600; letter-spacing: 1px; }
  .cta-starvation { left: 58px; background: linear-gradient(var(--orange-light), var(--orange)); border-color: #eea33a; }
  .cta-why { left: 359px; background: linear-gradient(var(--blue-top), var(--blue-bottom)); border-color: #3d63b8; padding-left: 10px; }
  .cta-burner { left: 659px; background: linear-gradient(var(--green-top), var(--green-bottom)); border-color: #7dbd33; padding-left: 14px; }

  .welcome { position: absolute; left: 57px; top: 716px; width: 590px; }
  .welcome h1 { color: var(--welcome-green); font-size: 26px; font-weight: 500; letter-spacing: 0.5px; margin-bottom: 8px; }
  .welcome p { margin-left: 13px; width: 570px; font-size: 12px; line-height: 15px; letter-spacing: 0.45px; margin-bottom: 22px; }

  .testimonials { position: absolute; left: 661px; top: 701px; width: 279px; height: 284px; border-radius: 18px;
    background: var(--panel-grey); overflow: hidden; }
  .testimonials h2 { height: 44px; background: var(--green-top); color: var(--white); font-size: 20px; font-weight: 500;
    letter-spacing: 0.5px; padding: 10px 0 0 19px; text-shadow: 1px 1px 2px rgba(0,0,0,0.35); }
  .testimonials p { padding: 18px 22px 0 17px; font-size: 12px; line-height: 15px; letter-spacing: 0.45px; }
  .read-more { position: absolute; right: 36px; bottom: 10px; color: var(--orange); font-size: 12px; text-decoration: none; }

  .site-footer { position: absolute; left: 0; top: 1000px; width: 1000px; height: 200px; background: var(--teal);
    color: var(--white); font-size: 13px; letter-spacing: 0.6px; text-align: center; }
  .footer-links { padding-top: 28px; }
  .footer-links a { color: var(--white); text-decoration: none; }
  .footer-links .sep { margin: 0 21px; }
  .copyright { margin-top: 36px; }
</style>
</head>
<body>
  <header class="site-header">
    <div class="brand"><span>Coral Bayslim</span><span class="brand-dot"></span></div>
  </header>

  <nav class="main-nav">
    <a class="nav-tab is-active" style="left:50px;width:225px">Science of<br>Weight Loss Success</a>
    <a class="nav-tab" style="left:275px;width:170px">Success Stories</a>
    <a class="nav-tab" style="left:445px;width:215px">Location and Hours</a>
    <a class="nav-tab" style="left:660px;width:135px">Contact Us</a>
    <a class="nav-tab" style="left:795px;width:155px">Espanol</a>
    <span class="nav-end"></span>
  </nav>

  <section class="hero">
    <p class="slogan">Your Slogan<span>goes Here...</span></p>
    <div class="hero-photo" role="img" aria-label="Stock photo of a fit woman in a pink sports top measuring her waist"></div>
  </section>

  <a class="cta cta-starvation">Stop the<br><strong>LOW CALORIE</strong><br>Starvation Diet</a>
  <a class="cta cta-why">Why<br>CORAL BAYSLIM</a>
  <a class="cta cta-burner">Become a Skinny<br>FAT BURNER<br>Today</a>

  <main class="welcome">
    <h1>Welcome to Coral Bayslim</h1>
    <p>Lorem Ipsum is simply dummy text of the printing and typesetting industry. Lorem Ipsum has been the industry's standard dummy text ever since the 1500s, when an unknown printer took a galley of type and scrambled it to make a type specimen book. It has survived not only five centuries, but also the leap into electronic typesetting, remaining essentially unchanged. It was popularised in the 1960s with the release of Pressline sheets containing Lorem Ipsum passages, and more recently with desktop publishing software like Orvin PageSetter including versions of Lorem Ipsum.</p>
    <p>Lorem Ipsum is simply dummy text of the printing and typesetting industry. Lorem Ipsum has been the industry's standard dummy text ever since the 1500s, when an unknown printer took a galley of type and scrambled it to make a type specimen book. It has survived not only five centuries, but also the leap into electronic typesetting, remaining essentially unchanged. It was popularised in the 1960s with the release of Pressline sheets containing Lorem Ipsum passages, and more recently with desktop publishing software like Orvin PageSetter including versions of Lorem Ipsum.</p>
  </main>

  <aside class="testimonials">
    <h2>Testimonials</h2>
    <p>Lorem Ipsum is simply dummy text of the printing and typesetting industry. Lorem Ipsum has been the industry's standard dummy text ever since the 1500s, when an unknown printer took a galley of type and scrambled it to make a type specimen book. It has survived not only five centuries, but also the leap into electronic typesetting, remaining essentially unchanged.</p>
    <a class="read-more">Read More...</a>
  </aside>

  <footer class="site-footer">
    <div class="footer-links">
      <a>Science of Weight Loss Success</a><span class="sep">|</span>
      <a>Success Stories</a><span class="sep">|</span>
      <a>Location and Hours</a><span class="sep">|</span>
      <a>Contact Us</a><span class="sep">|</span>
      <a>Espanol</a>
    </div>
    <p class="copyright">© 2014 Coral Bayslim</p>
  </footer>
</body>
</html>
```